Need new website for my business

I want to design a new Irrigation website for our business. What we are looking for is to have a residential section that describes providing for irrigation service for residential customers in homeowners Association. From startups to service to winterization in full residential installs.
A commercial section on our webpage describing. installation of commercial Irrigation systems. Service start-up of systems. To winterizations. Offering contract service plans for commercial customers.
Service for both commercial residential include making sure all zones are operating check for leaks adjust spray nozzles in rotors making sure all irrigation heads rotate, and are not stuck or damaged making sure that we have full coverage of each Irrigation zone for lawns. In all drip irrigation is Functioning in watering the plants accordingly. Adjusting control settings to make sure you have the right watering times during the hot dry months.
Have a landscape lighting tab:
Describing what landscape lighting and what it does to enhance curb, appeal, highlight architectural, features of landscape and transferring your outdoor space into inviting visual stunning areas with low-voltage landscape lighting
And a residential snow plowing for the Falmouth Maine area. In commercial snow, plowing and snow removal covering Scarborough south portland Portland Falmouth in Cumberland Maine for commercial Snow services. From plow & Salting parking lots to Snow removing, and Snow displacement.
we started a website but it needs a up lift and bring it to pop
our web site is willowbrookyards314.com
here are a few websites that we really like:
www.sprinklecoastal.com
www.dewpointwatering.com
www.verdantlawnsystems.com
Industry/Entity Type
Irrigation & Landscape Lighting
Coding
Coded - Design and coding required
Number of Pages Required
4 page

```html
<!DOCTYPE html>
<html lang="en">
<head>
<meta charset="utf-8">
<title>Willowbrook Irrigation &amp; Lighting – Home and Lighting Pages</title>
<link href="https://fonts.googleapis.com/css2?family=Crimson+Pro:wght@500;600&family=Open+Sans:wght@400;600;700&display=swap" rel="stylesheet">
<style>
  :root {
    --board: #8c8c8c;
    --white: #ffffff;
    --navy: #1b2b48;
    --navy-text: #1f2c45;
    --green: #4cb332;
    --green-dark: #3f9e2a;
    --ice: #dff5f5;
    --icon-teal: #2c9aa6;
    --muted: #c9d1de;
    --sky-top: #5f7590;
    --sky-glow: #d9935a;
    --tree: #2f4a2a;
    --lawn: #4d7a2e;
    --lawn-deep: #335a1f;
  }
  * { box-sizing: border-box; margin: 0; padding: 0; }
  html, body { width: 803px; height: 1200px; overflow: hidden; }
  body { background: var(--board); font-family: "Open Sans", sans-serif; position: relative; }

  .page { position: absolute; left: 59px; width: 688px; background: var(--white); overflow: hidden; }
  .page--home { top: 32px; height: 596px; }
  .page--lighting { top: 695px; height: 480px; background: var(--navy); }

  .site-header { position: absolute; left: 0; top: 0; width: 100%; height: 61px; background: var(--white); }
  .brand { position: absolute; left: 30px; top: 14px; }
  .brand__name { font-family: "Open Sans", sans-serif; font-weight: 700; font-size: 22px; line-height: 24px; color: var(--green); letter-spacing: -0.3px; }
  .brand__tag { font-size: 6px; color: #6c8fc0; margin-top: 1px; letter-spacing: 0.2px; }
  .nav { position: absolute; top: 24px; font-size: 8px; font-weight: 600; color: var(--navy-text); }
  .nav--home { left: 391px; }
  .nav--services { left: 443px; }
  .nav--lighting { left: 521px; }
  .btn { position: absolute; background: var(--green); color: var(--white); font-size: 7px; font-weight: 700; display: flex; align-items: center; justify-content: center; border-radius: 2px; }
  .btn--header { left: 575px; top: 19px; width: 81px; height: 24px; }

  .hero { position: absolute; left: 0; top: 61px; width: 100%; height: 260px;
    background: linear-gradient(180deg, var(--sky-top) 0%, #8b8f98 22%, var(--sky-glow) 36%, var(--tree) 46%, var(--lawn) 58%, var(--lawn-deep) 100%); }
  .hero__title { position: absolute; left: 102px; top: 36px; font-family: "Crimson Pro", serif; font-weight: 500; font-size: 38px; line-height: 43px; color: var(--white); }
  .hero__sub { position: absolute; left: 102px; top: 175px; font-size: 11px; color: #e8eee4; }
  .btn--hero { left: 101px; top: 207px; width: 75px; height: 25px; }

  .why { position: absolute; left: 0; top: 321px; width: 100%; height: 218px; }
  .why__title { position: absolute; left: 161px; top: 27px; font-family: "Crimson Pro", serif; font-weight: 600; font-size: 16px; color: var(--navy-text); }
  .feature { position: absolute; top: 63px; width: 96px; text-align: center; }
  .feature__badge { width: 67px; height: 67px; margin: 0 auto; border-radius: 50%; background: var(--ice); display: flex; align-items: center; justify-content: center; }
  .feature__label { margin-top: 14px; font-size: 8px; line-height: 12px; color: var(--navy-text); }

  .site-footer { position: absolute; left: 0; top: 539px; width: 100%; height: 57px; background: var(--navy); color: var(--muted); }
  .footer__heading { position: absolute; left: 110px; top: 10px; font-size: 8px; font-weight: 600; color: #e4e9f1; }
  .footer__text { position: absolute; left: 110px; top: 24px; width: 160px; font-size: 5.5px; line-height: 9px; }
  .footer__meta { position: absolute; left: 110px; top: 45px; font-size: 5px; }
  .footer__nav { position: absolute; top: 14px; font-size: 7px; color: #e4e9f1; }
  .footer__dot { position: absolute; top: 14px; width: 12px; height: 12px; border: 3px solid var(--green); border-radius: 50%; }

  .lighting__title { position: absolute; left: 83px; top: 150px; font-family: "Crimson Pro", serif; font-weight: 500; font-size: 38px; color: var(--white); }
  .lighting__sub { position: absolute; left: 84px; top: 203px; font-size: 15px; color: #d9dfe8; }
  .lighting__body { position: absolute; left: 83px; top: 275px; width: 500px; font-size: 14px; line-height: 22px; color: #d3d9e3; }
  .benefit { position: absolute; top: 405px; width: 60px; text-align: center; }
  .benefit__label { margin-top: 8px; font-size: 8px; font-weight: 600; color: #d3d9e3; }
  .photo { position: absolute; top: 387px; height: 93px; }
  .photo--front { left: 315px; width: 138px; background: linear-gradient(180deg, #4f6b8c 0%, #8b7a4e 45%, #3c5a2c 80%, #56763a 100%); }
  .photo--side { left: 462px; width: 139px; background: linear-gradient(180deg, #6d8fb8 0%, #7f7a5d 45%, #3f5c2f 78%, #5e7c40 100%); }
</style>
</head>
<body>

<section class="page page--home">
  <header class="site-header">
    <div class="brand">
      <div class="brand__name">willowbrook</div>
      <div class="brand__tag">Irrigation, Lighting &amp; Snow Services</div>
    </div>
    <span class="nav nav--home">Home</span>
    <span class="nav nav--services">Irrigation Services</span>
    <span class="nav nav--lighting">Lighting</span>
    <span class="btn btn--header">Get a Quote</span>
  </header>

  <div class="hero" role="img" aria-label="Photo of a green lawn at sunset with sprinklers spraying water, trees on the horizon">
    <h1 class="hero__title">Caring for your<br>green oasis<br>in Maine</h1>
    <p class="hero__sub">Experts in Irrigation, Lighting &amp; Snow Removal</p>
    <span class="btn btn--hero">Learn More</span>
  </div>

  <div class="why">
    <h2 class="why__title">Why Choose Us</h2>
    <div class="feature" style="left:200px">
      <div class="feature__badge">
        <svg width="28" height="34" viewBox="0 0 28 34" fill="none" stroke="#1f2c45" stroke-width="1.8"><path d="M14 2 C14 2 3 16 3 22 a11 11 0 0 0 22 0 C25 16 14 2 14 2Z"/><path d="M11 23 a3 3 0 0 0 6 0"/></svg>
      </div>
      <div class="feature__label">Water Smart<br>Technology</div>
    </div>
    <div class="feature" style="left:296px">
      <div class="feature__badge">
        <svg width="36" height="36" viewBox="0 0 36 36" fill="none" stroke="#1f2c45" stroke-width="1.8"><path d="M6 32 L20 16 a7 7 0 0 1 9-9 l-4 5 2 3 4-3 a7 7 0 0 1-9 9 L9 35 Z"/></svg>
      </div>
      <div class="feature__label">Professional<br>Maintenance</div>
    </div>
    <div class="feature" style="left:392px">
      <div class="feature__badge">
        <svg width="36" height="36" viewBox="0 0 36 36" fill="none" stroke="#1f2c45" stroke-width="1.8"><circle cx="18" cy="18" r="5"/><path d="M18 4 v4 M18 28 v4 M4 18 h4 M28 18 h4 M8 8 l3 3 M25 25 l3 3 M8 28 l3-3 M25 11 l3-3"/><circle cx="18" cy="18" r="10"/></svg>
      </div>
      <div class="feature__label">Customized<br>Scheduling</div>
    </div>
    <div class="feature" style="left:488px">
      <div class="feature__badge">
        <svg width="34" height="34" viewBox="0 0 34 34" fill="none" stroke="#1f2c45" stroke-width="1.8"><rect x="3" y="6" width="28" height="25" rx="2"/><path d="M3 12 h28 M10 3 v6 M24 3 v6 M11 18 v8 h5 M20 18 v8 M20 18 h5 M20 22 h4"/></svg>
      </div>
      <div class="feature__label">Organized<br>Scheduling</div>
    </div>
  </div>

  <footer class="site-footer">
    <div class="footer__heading">Contact Us Today</div>
    <p class="footer__text">Serving homes and businesses across Maine with care in every season.</p>
    <div class="footer__meta">willowbrookyards314.com</div>
    <span class="footer__nav" style="left:374px">Home</span>
    <span class="footer__nav" style="left:415px">Services</span>
    <span class="footer__nav" style="left:472px">Lighting</span>
    <span class="footer__dot" style="left:529px"></span>
    <span class="footer__dot" style="left:560px"></span>
  </footer>
</section>

<section class="page page--lighting">
  <header class="site-header">
    <div class="brand">
      <div class="brand__name">willowbrook</div>
      <div class="brand__tag">Irrigation, Lighting &amp; Snow Services</div>
    </div>
    <span class="nav nav--home">Home</span>
    <span class="nav nav--services">Irrigation Services</span>
    <span class="nav nav--lighting">Lighting</span>
    <span class="btn btn--header">Get a Quote</span>
  </header>

  <h1 class="lighting__title">Illuminate Your World</h1>
  <p class="lighting__sub">Low-Voltage Landscape Lighting</p>
  <p class="lighting__body">Enhance your curb appeal, highlight architectural features, and create inviting, stunning spaces from your outdoor spaces.</p>

  <div class="benefit" style="left:80px">
    <svg width="22" height="32" viewBox="0 0 22 32" fill="none" stroke="#2c9aa6" stroke-width="2"><path d="M7 2 h8 M5 6 h12 v22 H5 Z"/><rect x="8" y="12" width="6" height="9" rx="1"/></svg>
    <div class="benefit__label">Efficiency</div>
  </div>
  <div class="benefit" style="left:154px">
    <svg width="28" height="32" viewBox="0 0 28 32" fill="none" stroke="#2c9aa6" stroke-width="2"><path d="M14 2 L26 6 V15 C26 23 20 28 14 30 C8 28 2 23 2 15 V6 Z"/><circle cx="14" cy="15" r="4"/></svg>
    <div class="benefit__label">Quality</div>
  </div>
  <div class="benefit" style="left:228px">
    <svg width="30" height="34" viewBox="0 0 30 34" fill="none" stroke="#2c9aa6" stroke-width="2"><path d="M15 2 L28 6 V16 C28 25 21 30 15 32 C9 30 2 25 2 16 V6 Z"/><path d="M17 10 L13 18 h4 l-3 7"/></svg>
    <div class="benefit__label">Security</div>
  </div>

  <div class="photo photo--front" role="img" aria-label="Photo of a large house at dusk lit by warm landscape lighting"></div>
  <div class="photo photo--side" role="img" aria-label="Photo of a home among trees with illuminated facade and lawn"></div>
</section>

</body>
</html>
```